Vegan Alfredo Sauce Label Design for Bramble Pantry Co

We are a food co. committed to making vegan food more accessible to people who want to eat healthier. Our first line of product is vegan Alfredo sauce.
We have 3 flavors:
- Garlic
- Pesto
- Lemony Artichoke
The current project is the design for the first flavor: garlic. However, we would like a template that would translate well to other flavors, so they look like a family of products.
These will be in standard 16 oz jars. The whole label will be approx 6cm x 24cm, but the front visual space is approx 6cm x 10cm. The rest will be nutritional labeling and copy about the company.
We also need a stamp or font- based logo that says Bramble Pantry Co. (or lower case: bramble pantry co.), the name of the company.
The picture (attached) of Vegan Mimbo is the closest to what we are going for. Because the sauce is creamy white, a colorful background with off-white font will be best.
We currently have a website, although we are doing a brand over-haul (hence, this posting) www.bramblepantryco-example.com. If the designer is a good fit, we have several more projects, in line.
Other brands we love: Tidy Acres, Marlow Ridge Foods, Pulp Poured Daily.
The final brand should communicate hip, natural and health.
And personally, I love design that is clever and somehow makes me smile.
Target Market(s)
Vegans, vegetarians, and people with common food allergies - all ages.
Young, hip families.
Industry/Entity Type
It Company
Requirements
Must have
- Copy:
Vegan Alfredo or Vegan Alfredo Sauce
Garlic
Bramble Pantry or Bramble Pantry Co
16 oz
Nice to have
- May include copy:
Gluten-Free Soy-Free Nut-Free
Should not have
- Neon colors

```html
<!DOCTYPE html>
<html lang="en">
<head>
<meta charset="utf-8">
<title>Vegan Alfredo Sauce – Bramble Pantry Co</title>
<link rel="stylesheet" href="https://fonts.googleapis.com/css2?family=Marcellus&family=Arvo:wght@700&family=Open+Sans:wght@400;600&display=swap">
<style>
  :root {
    --page: #f3f3f1;
    --label-red: #921c2e;
    --cream: #fbf7ea;
    --white: #ffffff;
    --leaf: #7cc242;
    --leaf-deep: #3fa535;
    --leaf-light: #a6d86a;
    --ribbon-shade: #d9d9d9;
  }
  * { margin: 0; padding: 0; box-sizing: border-box; }
  html, body { width: 1200px; height: 796px; overflow: hidden; }
  body { background: var(--page); position: relative; font-family: "Open Sans", sans-serif; }

  .label {
    position: absolute; left: 197px; top: 139px;
    width: 839px; height: 506px;
    background: var(--label-red);
    border: 3px solid var(--white);
    box-shadow: 0 2px 8px rgba(0,0,0,0.18);
    overflow: hidden;
  }
  .hill-layer, .type-layer { position: absolute; left: 0; top: 0; }
  .hill-layer { z-index: 0; }
  .type-layer { z-index: 3; }

  .allergen-line {
    position: absolute; top: 18px; left: 0; width: 100%;
    text-align: center; color: var(--cream);
    font-size: 8px; letter-spacing: 0.3px; z-index: 3;
  }
  .badge {
    position: absolute; left: 362px; top: 48px;
    width: 108px; height: 108px; border-radius: 50%;
    background: var(--white); z-index: 1;
    display: flex; align-items: flex-start; justify-content: center;
    padding-top: 12px;
  }
  .badge-art {
    width: 70px; height: 72px; border-radius: 40%;
    background: radial-gradient(circle at 50% 50%, #f4cf55 0%, #efd078 45%, #ece6d4 75%, var(--white) 100%);
  }
  .farm-scene {
    position: absolute; left: 272px; top: 310px;
    width: 284px; height: 138px; border-radius: 45% 45% 12% 12%;
    background: linear-gradient(180deg, rgba(251,247,234,0) 0%, #f4ecc4 30%, #e9dba0 65%, #8fc95a 100%);
    z-index: 1;
  }
  .ribbon-word {
    font-family: "Arvo", serif; font-weight: 700; font-size: 31px;
    fill: var(--leaf); letter-spacing: 1px;
  }
  .title {
    font-family: "Marcellus", serif; font-size: 60px;
    fill: var(--cream); letter-spacing: 1px;
  }
  .flavor {
    font-family: "Open Sans", sans-serif; font-weight: 600; font-size: 15px;
    fill: var(--cream); letter-spacing: 4px;
  }
  .brand-name {
    position: absolute; top: 467px; left: 0; width: 100%;
    text-align: center; color: var(--cream);
    font-size: 14.5px; letter-spacing: 0.8px; z-index: 3;
  }
  .net-weight {
    position: absolute; top: 469px; right: 26px;
    color: var(--cream); font-size: 12px; font-weight: 600;
    letter-spacing: 0.8px; z-index: 3;
  }
</style>
</head>
<body>
  <div class="label">
    <svg class="hill-layer" width="839" height="506" viewBox="0 0 839 506" aria-hidden="true">
      <defs>
        <linearGradient id="hill-fill" x1="0" y1="0" x2="0" y2="1">
          <stop offset="0" stop-color="var(--leaf-light)"/>
          <stop offset="1" stop-color="var(--leaf-deep)"/>
        </linearGradient>
      </defs>
      <path d="M 40 506 Q 420 328 845 470 L 845 506 Z" fill="url(#hill-fill)"/>
      <path d="M 330 506 Q 620 430 845 480 L 845 492 Q 620 450 380 506 Z" fill="var(--leaf)" opacity="0.7"/>
    </svg>

    <p class="allergen-line">GLUTEN-FREE, SOY-FREE, NUT-FREE</p>
    <div class="badge"><div class="badge-art" role="img" aria-label="Illustration of a milk jug, a wedge of cheese and garlic bulbs"></div></div>
    <div class="farm-scene" role="img" aria-label="Illustration of a cream barn with a tree and a windmill on a green hill"></div>

    <svg class="type-layer" width="839" height="506" viewBox="0 0 839 506" aria-hidden="true">
      <defs>
        <path id="title-arc" d="M 170 300 Q 419 236 668 300"/>
      </defs>
      <path d="M 299 158 L 330 154 L 330 196 L 299 200 L 311 178 Z" fill="var(--ribbon-shade)"/>
      <path d="M 539 158 L 508 154 L 508 196 L 539 200 L 527 178 Z" fill="var(--ribbon-shade)"/>
      <path d="M 322 150 Q 419 140 516 150 L 516 192 Q 419 182 322 192 Z" fill="var(--white)"/>
      <text class="ribbon-word" x="419" y="181" text-anchor="middle">VEGAN</text>
      <text class="title"><textPath href="#title-arc" startOffset="50%" text-anchor="middle">ALFREDO SAUCE</textPath></text>
      <text class="flavor" x="421" y="300" text-anchor="middle">GARLIC</text>
    </svg>

    <p class="brand-name">BRAMBLE PANTRY CO</p>
    <p class="net-weight">16 OZ</p>
  </div>
</body>
</html>
```